Rivex Management LLC Business Card

The sample logo was attached for the business Card Design for Traffic Control Company named Rivex Management LLC. Card design needs to have the company logo and colors match the logo color. It will be nice to show some images of Traffic control signs or cones, even roads closer that math the company services

Target Market(s)

Temporary traffic control. Road closer.

Industry/Entity Type

Construction

Contact Information for Business Card

basic information, name, job title, address, email phone, website

Font styles to use
Serif
Sans Serif

Colors
F0912C
F2A743
F7CA91
FBE8D2
FDF5EE
EE7325
F08F49
F5BC92
FAE3D3
FDF4ED

```html
<!DOCTYPE html>
<html lang="en">
<head>
<meta charset="utf-8">
<title>Rivex Management LLC Business Card</title>
<link href="https://fonts.googleapis.com/css2?family=Lato:wght@400;700;900&display=swap" rel="stylesheet">
<style>
  :root {
    --stage: #2b2b2d;
    --card-dark: #1d1e20;
    --orange: #ee7325;
    --white: #ffffff;
    --rule: #6b6b6b;
    --road-top: #5a5a5c;
    --road-bottom: #3e3f41;
  }
  * { box-sizing: border-box; margin: 0; padding: 0; }
  html, body { width: 1200px; height: 1108px; overflow: hidden; }
  body {
    background: var(--stage);
    font-family: 'Lato', sans-serif;
    display: flex;
    align-items: center;
    justify-content: center;
    gap: 60px;
  }
  .card {
    width: 420px;
    height: 720px;
    border-radius: 22px;
    overflow: hidden;
    position: relative;
  }
  .card--front {
    background: var(--card-dark);
    color: var(--white);
    display: flex;
    flex-direction: column;
    align-items: center;
    text-align: center;
  }
  .brand {
    margin-top: 150px;
    font-weight: 900;
    font-size: 44px;
    line-height: 1.1;
    color: var(--orange);
    letter-spacing: 1px;
    text-transform: uppercase;
  }
  .brand span { display: block; font-size: 26px; letter-spacing: 4px; }
  .person { margin-top: 120px; }
  .person__name {
    color: var(--orange);
    font-weight: 700;
    font-size: 30px;
    letter-spacing: 1px;
    text-transform: uppercase;
  }
  .person__title { font-size: 21px; margin-top: 2px; }
  .icon-row {
    display: flex;
    align-items: center;
    gap: 8px;
    margin-top: 18px;
    width: 290px;
  }
  .icon-row::before, .icon-row::after {
    content: ""; flex: 1; height: 1px; background: var(--rule);
  }
  .icon {
    width: 32px; height: 32px;
    background: var(--orange);
    border-radius: 5px;
    display: flex; align-items: center; justify-content: center;
  }
  .contact { margin-top: 12px; font-size: 21px; line-height: 1.35; }
  .divider { width: 290px; height: 1px; background: var(--rule); margin: 14px 0; }
  .address { font-size: 21px; line-height: 1.35; }
  .card--back {
    background: linear-gradient(180deg, var(--road-top) 0%, var(--road-bottom) 100%);
  }
  .card--back .scene {
    position: absolute; inset: 0 0 240px 0;
    background:
      radial-gradient(ellipse at 60% 15%, rgba(238,115,37,.55), transparent 55%),
      radial-gradient(ellipse at 40% 65%, rgba(238,115,37,.35), transparent 50%),
      linear-gradient(180deg, #6a6a6c, #4a4b4d);
  }
  .card--back .brand {
    position: absolute; left: 0; right: 0; bottom: 110px;
    margin: 0; text-align: center;
  }
  .card--back .brand span { color: var(--orange); }
</style>
</head>
<body>
  <section class="card card--front">
    <div class="brand">Rivex<span>Management LLC</span></div>
    <div class="person">
      <div class="person__name">Daniel Morrow</div>
      <div class="person__title">Managing Director</div>
    </div>
    <div class="icon-row">
      <div class="icon">
        <svg width="18" height="18" viewBox="0 0 24 24"><path fill="#1d1e20" d="M6.6 10.8a15 15 0 0 0 6.6 6.6l2.2-2.2a1 1 0 0 1 1-.25 11.4 11.4 0 0 0 3.6.57 1 1 0 0 1 1 1V20a1 1 0 0 1-1 1A17 17 0 0 1 3 4a1 1 0 0 1 1-1h3.5a1 1 0 0 1 1 1c0 1.25.2 2.45.57 3.6a1 1 0 0 1-.25 1z"/></svg>
      </div>
      <div class="icon">
        <svg width="18" height="18" viewBox="0 0 24 24"><rect x="3" y="5" width="18" height="14" rx="1" fill="none" stroke="#1d1e20" stroke-width="2"/><path d="M3 6l9 7 9-7" fill="none" stroke="#1d1e20" stroke-width="2"/></svg>
      </div>
      <div class="icon">
        <svg width="18" height="18" viewBox="0 0 24 24"><circle cx="12" cy="12" r="9" fill="none" stroke="#1d1e20" stroke-width="2"/><path d="M3 12h18M12 3c3 3 3 15 0 18M12 3c-3 3-3 15 0 18" fill="none" stroke="#1d1e20" stroke-width="1.6"/></svg>
      </div>
    </div>
    <div class="contact">
      <div>044-987 650 312</div>
      <div>info@rivexmgmt.com</div>
      <div>www.rivexmgmt.com</div>
    </div>
    <div class="divider"></div>
    <div class="address">
      <div>421, Address line here</div>
      <div>45452, Country Name</div>
    </div>
  </section>

  <section class="card card--back">
    <div class="scene" role="img" aria-label="Photograph of rows of orange and white traffic cones on grey paving"></div>
    <div class="brand">Rivex<span>Management LLC</span></div>
  </section>
</body>
</html>
```